Tides & Ember novel and CD cover designs
"Make dreams come true" theme
Tides & Ember novel and CD cover designs -
Creative Brief
NOVEL TITLE: Tides & Ember AUTHOR: Lorna Pettigrew Sallow GENRE: women’s fiction LENGTH: 114,000-words THEME: making dreams come true Paranormal element: heroine’s dreams are guiding her (one actually comes true in real life, which makes her see she should listen to her intuitions) SETTING: Half of the story takes place in 1977–78 in Coeur d’Alene, ID, half in 2003 (mostly) in California CHARACTERS: (see list at end) SYNOPSIS: Witnessing a horrific car accident makes award-winning singer Josephine Marlow reevaluate her empty Hollywood lifestyle. Spurred by recurring dreams and near-forgotten longings, she returns to Coeur d’Alene, Idaho, with the hopes of reconnecting with her old love and former singing partner Neil Fenwick. But, he spurns her despite her efforts to reconcile. In the end, she discovers her true passion lies in sharing music and, in her attempt to win back Neil’s love, she is able to reconnect with the innocent enjoyment of music they once enjoyed together. She moves forward to teach and share music, finding true fulfillment — and through that, winds up gaining her lost love after all. COMPACT DISK (CD) COVER TITLE: Tides & Ember SINGER/SONGWRITER: Lorna Pettigrew Sallow GENRE: folk and easy listening LENGTH: 5 original songs inspired by the novel TIDES & EMBER CHARACTERS JOSEPHINE MARLOW (heroine) • Striking/curly light blonde hair/green eyes/slim/5’4” • Practical, almost controlling • Disbelieving of intuitions at first, but comes to believe them • Driven • Talented vocalist • Honest • Loyal • Witty • Smart • In love with Neil NEIL FENWICK (hero) • Handsome/honey brown hair/hazel eyes/slim/5’10” • Talented composer/pianist • Frustrated with home responsibilities forced on him by his parents • Dreamer • Home-body • Loner • Loves kids • Honest • Smart • In love with Josie, childhood friend of both Beth and Gordon GORDON WICK • Gorgeous/blonde/blue eyes/athletic/6’1” • Conniving and manipulative • Resourceful • Jock/Athletic • Smart • Loves action • In love w/ Josie, great friends and eventual husband of Beth BETH HOLLOWAY WICK • Pretty/brunette/brown eyes/lanky/5’7” • Follower at first, but comes into her own as a party planner as an adult • Loves catering and planning parties • Lost (in some ways), often looks for guidance • Smart • Loyal • Resourceful • In love with Neil for many years, marries Gordon, hates Josie until near end of story, former best friend of Miranda MIRANDA COLE PERIWELL • Plain/brunette/brown eyes/plump/5’6” • Insightful • Wise • Generous • Friendly • Funny • Josie’s best friend, in love with Todd TODD PERIWELL • Cute/ginger-haired/hazel eyes/wiry/5’9” • Funny • Friendly • Dorky • From Texas • In love with Miranda, friends with Josie
40-something+ women's fiction readers desiring to fulfill life dreams
NOVEL General design concepts to consider: • Prefer artist w/ book COVER DESIGN EXPERIENCE, as there are certain nuances which entice readers pick a book off a shelf • BOOK SIZE: Octavo, 9”X6” • A MUSIC BOX plays a key role in the story between the hero and heroine • The main image guiding the heroine in her dream is a SHAFT OF LIGHT shining on a lake cabin deck. • The CABIN also is a main theme. The structure overlooks the lake has one door, two porthole-shaped windows, a large deck, and a creek running under the deck. • CONCEPTS I LIKE: – Most of the image in black & white and punching it up w/ one main element in color, but I’m not tied to this idea. It appeals to me because it’s representative of the flashback element in the story. – An image reflected in someone’s eye – Half of a face – A shaft of light shining through a door or window to illuminate a key element (perhaps the music box) COMPACT DISK (CD) General design concepts to consider: • Must be adapted from book cover design • Music files will be MP3 format, but may also be printed on physical CD, so need image that will fit in a CD jewel box, or can be printed on CD sleeve. (4.724 inches square, or 4.974 inches square for "bleeds.")

```html
<!DOCTYPE html>
<html lang="en">
<head>
<meta charset="UTF-8">
<title>Tides &amp; Ember — CD Label</title>
<link href="https://fonts.googleapis.com/css2?family=Crimson+Pro:wght@400;700&display=swap" rel="stylesheet">
<style>
  :root {
    --page-bg: #ffffff;
    --art-canopy: #26332b;
    --art-stone: #5f6a66;
    --art-foliage: #3f5a3c;
    --art-glow: #c9a86e;
    --art-water: #6f8f98;
    --art-shore: #2c3d3f;
    --title-ink: #ffffff;
    --credit-ink: #f4f1ea;
  }
  html, body {
    margin: 0;
    width: 1200px;
    height: 890px;
    overflow: hidden;
    background: var(--page-bg);
  }
  .canvas {
    position: relative;
    width: 1200px;
    height: 890px;
  }
  .disc {
    position: absolute;
    left: 160px;
    top: 20px;
    width: 860px;
    height: 860px;
  }
  .disc-art {
    position: absolute;
    inset: 0;
  }
  .disc-title {
    position: absolute;
    left: 340px;
    top: 188px;
    margin: 0;
    font-family: "Crimson Pro", Georgia, serif;
    font-weight: 400;
    font-size: 100px;
    line-height: 86px;
    color: var(--title-ink);
    text-shadow: 0 2px 8px rgba(0,0,0,0.4);
    white-space: nowrap;
  }
  .disc-title .line-two {
    display: block;
    padding-left: 30px;
  }
  .disc-credit {
    position: absolute;
    left: 565px;
    top: 622px;
    transform: translateX(-50%);
    margin: 0;
    font-family: "Crimson Pro", Georgia, serif;
    font-weight: 700;
    font-size: 22px;
    color: var(--credit-ink);
    white-space: nowrap;
    text-shadow: 0 1px 4px rgba(0,0,0,0.5);
  }
</style>
</head>
<body>
  <main class="canvas">
    <section class="disc">
      <svg class="disc-art" width="860" height="860" viewBox="0 0 860 860">
        <defs>
          <linearGradient id="sceneTone" x1="0.2" y1="0" x2="0.45" y2="1">
            <stop offset="0" stop-color="var(--art-canopy)"/>
            <stop offset="0.22" stop-color="var(--art-stone)"/>
            <stop offset="0.45" stop-color="var(--art-foliage)"/>
            <stop offset="0.62" stop-color="var(--art-glow)"/>
            <stop offset="0.78" stop-color="var(--art-water)"/>
            <stop offset="1" stop-color="var(--art-shore)"/>
          </linearGradient>
          <mask id="spindleHole">
            <rect width="860" height="860" fill="#fff"/>
            <circle cx="430" cy="455" r="67" fill="#000"/>
          </mask>
        </defs>
        <circle class="disc-scene" cx="430" cy="430" r="430" fill="url(#sceneTone)" mask="url(#spindleHole)"
          role="img" aria-label="Illustration: a veiled robed figure stands before a vine-covered stone archway opening onto a glowing lake at dusk, framed by green foliage and sparkling lights"/>
      </svg>
      <h1 class="disc-title">Tides<span class="line-two">&amp; Ember</span></h1>
      <p class="disc-credit">Lorna Pettigrew Sallow</p>
    </section>
  </main>
</body>
</html>
```